Educational clinic needs a new webpage design

I have a relatively new website but I am unhappy with the design. I was hoping the look of it would more match my logo, brochures, business cards, and postcards. The content is good and it's already mobile ready. The designer used square space, which I would like to keep if possible. My website is www.willowgatestudio.com

Target Market(s)

Parents of school age children

Industry/Entity Type

Education

Number of Pages Required

5+ page

Requirements
Must have
• Pictures must depict the diversity of our students. We service all ages, from preschool through college and our students come from varying races.
Should not have
• I try to avoid the word "tutoring" because what we do is so much more. I like the tag line of "results that go beyond traditional tutoring"

```html
<!DOCTYPE html>
<html lang="en">
<head>
<meta charset="utf-8">
<title>Willowgate Learning Studio</title>
<link href="https://fonts.googleapis.com/css2?family=Josefin+Sans:wght@400;600;700&family=Open+Sans:wght@400;600;700&display=swap" rel="stylesheet">
<style>
:root{
  --purple:#5c2d84;
  --purple-dark:#4a2270;
  --green:#8cc63f;
  --navy:#1f2b3b;
  --navy-deep:#18222f;
  --ink:#222;
  --muted:#777;
  --soft:#f3f3f3;
  --line:#e2e2e2;
  --white:#fff;
}
*{box-sizing:border-box;margin:0;padding:0}
html,body{width:1200px;height:4358px;overflow:hidden}
body{position:relative;background:var(--white);font-family:"Open Sans",Arial,sans-serif;color:var(--ink)}
.abs{position:absolute}
.heading{font-family:"Josefin Sans",Arial,sans-serif;font-weight:700}
.photo{position:absolute}

/* header */
.topbar-icons{top:14px;right:40px;display:flex;gap:10px}
.topbar-icons span{width:12px;height:12px;border-radius:50%;background:#555;display:block}
.brand{top:40px;left:46px;display:flex;align-items:center;gap:12px}
.brand-dot{width:60px;height:60px;border-radius:50%;background:var(--purple)}
.brand-name{font-family:"Josefin Sans",sans-serif;font-weight:700;font-size:28px;color:var(--purple);line-height:1.05;width:300px}
.brand-tagline{top:112px;left:118px;font-size:11px;font-weight:600;color:#555;letter-spacing:.5px;white-space:nowrap}
.email-box{top:60px;left:545px;display:flex;align-items:center;gap:12px}
.email-icon{width:42px;height:42px;background:var(--purple);display:flex;align-items:center;justify-content:center}
.email-box small{display:block;font-size:13px;color:var(--muted)}
.email-box b{font-size:15px;color:var(--ink);font-weight:600}
.auth{top:68px;right:43px;display:flex;gap:12px}
.auth a{font-size:14px;padding:7px 16px;border:2px solid var(--purple);color:var(--purple);text-decoration:none;font-weight:600}
.auth a.fill{background:var(--purple);color:#fff}

.nav{top:138px;left:0;width:1200px;height:44px;background:var(--purple);display:flex;align-items:center}
.nav a{color:#fff;text-decoration:none;font-size:14px;padding:0 26px;height:44px;line-height:44px;border-right:1px solid rgba(255,255,255,.25)}
.nav a:first-child{padding-left:46px}
.roll{position:absolute;right:43px;top:0;display:flex;height:44px}
.roll span{background:var(--green);color:#1b2b10;font-size:14px;width:218px;line-height:44px;padding-left:24px}
.roll b{background:var(--purple-dark);color:#fff;width:52px;text-align:center;line-height:44px;font-size:15px}

.hero{top:182px;left:0;width:1200px;height:524px;background:linear-gradient(100deg,#c9a27c 0%,#9a7a63 30%,#556070 60%,#c2c5c9 100%)}
.hero-title{top:488px;left:0;width:1200px;text-align:center;color:#fff;font-size:48px;line-height:54px;letter-spacing:1px;text-transform:uppercase;font-weight:700}
.hero-btn{top:600px;left:505px;width:190px;height:40px;background:#fff;color:var(--ink);font-size:15px;text-align:center;line-height:40px;border:2px solid var(--purple)}
.dots{top:660px;left:566px;display:flex;gap:14px}
.dots span{width:12px;height:12px;border-radius:50%;background:rgba(255,255,255,.55)}
.dots span:last-child{background:#fff}

/* intro */
.intro-title{top:748px;left:46px;width:620px;font-family:"Open Sans",sans-serif;font-size:30px;line-height:38px;font-weight:400}
.intro-sub{top:840px;left:46px;font-size:13px;color:var(--muted)}
.feature{width:290px}
.feature h4{font-size:13px;font-weight:700;text-transform:uppercase;display:flex;gap:14px;align-items:center;margin-bottom:18px}
.feature p{font-size:12px;line-height:20px;color:var(--muted);padding-left:46px}
.intro-frame{top:788px;left:699px;width:455px;height:412px;border:6px solid var(--purple);border-top:none;border-right:none}

/* sections */
.section-title{left:0;width:1200px;text-align:center;font-size:36px;color:var(--ink)}
.section-sub{left:0;width:1200px;text-align:center;font-size:14px;color:var(--muted)}
.divider{left:400px;width:400px;height:1px;background:var(--line)}
.divider::after{content:"";position:absolute;left:194px;top:-6px;width:12px;height:12px;border-radius:50%;border:1px solid var(--line);background:#fff}

.course{width:536px;height:268px;background:var(--soft)}
.course .txt{position:absolute;left:0;top:0;width:268px;height:268px;padding:22px 30px;border-top:3px solid var(--purple)}
.course .meta{font-size:10px;color:var(--purple);text-transform:uppercase;margin-bottom:16px}
.course .meta i{color:var(--green);font-style:normal}
.course h3{font-size:13px;font-weight:700;text-transform:uppercase;line-height:20px;margin-bottom:30px}
.course p{font-size:12px;line-height:19px;color:var(--muted)}
.course .tab{position:absolute;left:-22px;top:28px;width:22px;height:34px;background:var(--purple)}
.course .pic{left:268px;top:0;width:268px;height:268px}

.news{width:333px;height:495px;background:var(--soft)}
.news .pic{left:0;top:0;width:333px;height:198px;border-bottom:4px solid var(--purple)}
.news .body{position:absolute;top:226px;left:30px;right:24px}
.news .meta{font-size:10px;color:var(--muted);text-transform:uppercase;margin-bottom:22px}
.news h3{font-size:13px;font-weight:700;text-transform:uppercase;margin-bottom:20px}
.news p{font-size:12px;line-height:19px;color:var(--muted)}
.news .more{position:absolute;top:413px;left:30px;background:var(--purple);color:#fff;font-size:11px;font-weight:700;padding:9px 14px}

.plus-tile{background:linear-gradient(135deg,#7a4ea3,#5c2d84)}
.plus{left:100px;top:55px;width:66px;height:66px;border-radius:50%;background:var(--green);color:#fff;font-size:44px;text-align:center;line-height:64px}

/* contact */
.contact{top:3505px;left:0;width:1200px;height:853px;background:var(--navy)}
.contact-title{top:3530px;left:0;width:1200px;text-align:center;color:#fff;font-size:36px}
.c-col{top:3600px;width:260px;text-align:center;color:#8d97a5;font-size:14px;line-height:21px}
.c-icon{width:76px;height:76px;border-radius:50%;background:#2b384a;margin:0 auto 38px;display:flex;align-items:center;justify-content:center}
.query{top:3885px;left:46px;width:1108px;height:410px;background:#fff}
.query h2{position:absolute;top:36px;left:0;width:100%;text-align:center;font-size:34px}
.field{position:absolute;left:72px;width:510px;height:38px;background:var(--soft);font-size:12px;color:var(--muted);padding:11px 16px}
.message{position:absolute;left:600px;top:116px;width:480px;height:156px;background:var(--soft);font-size:12px;color:var(--muted);padding:11px 16px}
.submit{position:absolute;top:306px;left:462px;width:160px;height:46px;background:var(--purple);color:#fff;font-weight:700;font-size:15px;text-align:center;line-height:46px;letter-spacing:1px}
.footer{top:4300px;left:0;width:1200px;height:58px;background:#fff;border-top:1px solid var(--line)}
.footer p{position:absolute;left:56px;top:22px;font-size:12px;color:#666}
.pay-badge{position:absolute;right:46px;top:12px;width:96px;height:34px;border-radius:6px;background:#f3b541}
</style>
</head>
<body>

<header>
  <div class="abs topbar-icons" aria-hidden="true"><span></span><span></span><span></span><span></span><span></span><span></span></div>
  <div class="abs brand"><div class="brand-dot"></div><div class="brand-name">Willowgate Learning Studio</div></div>
  <p class="abs brand-tagline">Results that go beyond traditional tutoring</p>
  <div class="abs email-box">
    <div class="email-icon"><svg width="22" height="16" viewBox="0 0 22 16"><rect x="1" y="1" width="20" height="14" fill="none" stroke="#fff" stroke-width="2"/><path d="M1 1l10 8 10-8" fill="none" stroke="#fff" stroke-width="2"/></svg></div>
    <div><small>Email Contact</small><b>info@willowgatestudio.com</b></div>
  </div>
  <div class="abs auth"><a href="#">LOG UP</a><a href="#" class="fill">SIGN UP</a></div>
  <nav class="abs nav">
    <a href="#">Home</a><a href="#">Services</a><a href="#">About Us</a><a href="#">Blog</a><a href="#">Payments</a><a href="#">Contact us</a>
    <div class="roll"><span>Enter Roll Number</span><b>GO</b></div>
  </nav>
</header>

<section>
  <div class="photo hero" role="img" aria-label="Smiling students studying together in a bright classroom"></div>
  <h1 class="abs heading hero-title">Take the first step<br>to knowledge with us</h1>
  <div class="abs hero-btn">Read More About</div>
  <div class="abs dots"><span></span><span></span><span></span></div>
</section>

<section>
  <h2 class="abs intro-title">We offer guided learning programs for students of all ages and learning types.</h2>
  <p class="abs intro-sub">Having over 9 million students worldwide and more than 50,000 online courses available.</p>

  <div class="abs feature" style="top:900px;left:46px">
    <h4><svg width="24" height="24" viewBox="0 0 24 24"><path d="M6 3h12v5a6 6 0 0 1-12 0z M12 14v5 M8 21h8" fill="none" stroke="var(--purple)" stroke-width="2"/></svg>Highest Rated</h4>
    <p>Every lesson is shaped around the learner so each student grows with calm and steady confidence.</p>
  </div>
  <div class="abs feature" style="top:900px;left:376px">
    <h4><svg width="24" height="24" viewBox="0 0 24 24"><rect x="2" y="4" width="20" height="14" fill="none" stroke="var(--purple)" stroke-width="2"/><path d="M10 8l5 3-5 3z" fill="var(--purple)"/></svg>Online Training</h4>
    <p>Join live sessions from home with guided practice, shared notes and a mentor on every call.</p>
  </div>
  <div class="abs feature" style="top:1045px;left:46px">
    <h4><svg width="24" height="24" viewBox="0 0 24 24"><circle cx="12" cy="12" r="10" fill="none" stroke="var(--green)" stroke-width="2"/><path d="M2 12h20M12 2c4 4 4 16 0 20M12 2c-4 4-4 16 0 20" fill="none" stroke="var(--green)" stroke-width="1.5"/></svg>We Are Global</h4>
    <p>Families from many places learn with us, bringing fresh views and stories into every class.</p>
  </div>
  <div class="abs feature" style="top:1045px;left:376px">
    <h4><svg width="24" height="24" viewBox="0 0 24 24"><rect x="3" y="3" width="18" height="18" fill="none" stroke="#e8a33a" stroke-width="2"/><path d="M8 12l3 3 5-6" fill="none" stroke="#e8a33a" stroke-width="2"/></svg>Skilled Faculty</h4>
    <p>Our caring teachers hold deep subject skill and years of practice with learners of all kinds.</p>
  </div>

  <div class="abs intro-frame"></div>
  <div class="photo" style="top:770px;left:715px;width:439px;height:420px;background:linear-gradient(160deg,#d9c7a8,#8f7d9f 55%,#4e5b7a)" role="img" aria-label="Diverse group of students walking with books"></div>
</section>

<section>
  <h2 class="abs heading section-title" style="top:1258px">Most Popular Courses</h2>
  <p class="abs section-sub" style="top:1310px">Having over 9 million students worldwide and more than 50,000 online courses available.</p>
  <div class="abs divider" style="top:1356px"></div>

  <article class="abs course" style="top:1415px;left:46px">
    <div class="tab"></div>
    <div class="txt"><div class="meta">By Lena Harrow &nbsp;|&nbsp; <i>December 21, 2015</i></div><h3>Introduction JavaScript<br>for Beginners</h3><p>In this course, you'll explore the JavaScript programming language by creating an app.</p></div>
    <div class="photo pic" style="background:linear-gradient(135deg,#cfd9e4,#5d7391)" role="img" aria-label="Student coding on a laptop"></div>
  </article>
  <article class="abs course" style="top:1415px;left:616px">
    <div class="txt"><div class="meta">By Mara Quill &nbsp;|&nbsp; <i>December 21, 2015</i></div><h3>Learning and<br>Collaborating</h3><p>Interested in starting a business? This course will help you define your vision and discover opportunities to make it happen.</p></div>
    <div class="photo pic" style="background:linear-gradient(135deg,#f1eeea,#8a6b5c)" role="img" aria-label="Hands writing on paper at a desk"></div>
  </article>
  <article class="abs course" style="top:1723px;left:46px">
    <div class="tab"></div>
    <div class="txt"><div class="meta">By Theo Brannock &nbsp;|&nbsp; <i>December 21, 2015</i></div><h3>PHP Programming for<br>Beginners</h3><p>This tutorial will introduce you to PHP, a server-side scripting language you can use to make dynamic websites.</p></div>
    <div class="photo pic" style="background:linear-gradient(135deg,#e2ddd6,#6e6a66)" role="img" aria-label="Hands typing on a keyboard"></div>
  </article>
  <article class="abs course" style="top:1723px;left:616px">
    <div class="txt"><div class="meta">By Ivo Castell &nbsp;|&nbsp; <i>December 21, 2015</i></div><h3>How to Become a Good<br>Leadership</h3><p>Become an effective online learner and develop your online communication skills when working with others.</p></div>
    <div class="photo pic" style="background:linear-gradient(135deg,#e6e8ea,#7d8796)" role="img" aria-label="Teacher leading a small class"></div>
  </article>
</section>

<section>
  <h2 class="abs heading section-title" style="top:2034px">Online Education News</h2>
  <p class="abs section-sub" style="top:2086px">Having over 9 million students worldwide and more than 50,000 online courses available.</p>
  <div class="abs divider" style="top:2132px"></div>

  <article class="abs news" style="top:2185px;left:46px">
    <div class="photo pic" style="background:linear-gradient(135deg,#d7dadf,#6a7382)" role="img" aria-label="Students working at computers in a lab"></div>
    <div class="body"><div class="meta">By Admin &nbsp;|&nbsp; January 6, 2016</div><h3>Becoming a Better Developer</h3><p>The most common thought is that coding whether it be as a software developer or a web developer can be improve through the use of tools.</p></div>
    <div class="more">READ MORE</div>
  </article>
  <article class="abs news" style="top:2185px;left:433px">
    <div class="photo pic" style="background:linear-gradient(135deg,#e7c9a5,#8a5c4e)" role="img" aria-label="Students gathered around a table sharing ideas"></div>
    <div class="body"><div class="meta">By Admin &nbsp;|&nbsp; January 6, 2016</div><h3>Customers and Competitors</h3><p>A successful business relies heavily on people and networking. A good team and wider network is essential to success and growth.</p></div>
    <div class="more">READ MORE</div>
  </article>
  <article class="abs news" style="top:2185px;left:822px">
    <div class="photo pic" style="background:linear-gradient(135deg,#efe2d6,#a0553f)" role="img" aria-label="Hand marking answers on a test sheet"></div>
    <div class="body"><div class="meta">By Admin &nbsp;|&nbsp; January 6, 2016</div><h3>Learning and Collaborating</h3><p>You are probably used to learning online on a daily basis, including turning to your phone for information rather than referring to books.</p></div>
    <div class="more">READ MORE</div>
  </article>
</section>

<section>
  <h2 class="abs heading section-title" style="top:2722px">Photo Gallery</h2>
  <div class="photo plus-tile" style="top:2839px;left:46px;width:267px;height:204px" role="img" aria-label="Students in class with purple overlay">
    <div class="abs plus">+</div>
  </div>
  <div class="photo" style="top:2839px;left:325px;width:547px;height:204px;background:linear-gradient(120deg,#9b7a62,#d6b69a 50%,#7c5f4f)" role="img" aria-label="Lecture hall full of students"></div>
  <div class="photo" style="top:2839px;left:883px;width:271px;height:204px;background:linear-gradient(135deg,#e5d5c7,#8e5da0)" role="img" aria-label="Student smiling at a desk"></div>
  <div class="photo" style="top:3054px;left:46px;width:267px;height:206px;background:linear-gradient(135deg,#d8c6b3,#6d5f57)" role="img" aria-label="Group of students standing together"></div>
  <div class="photo" style="top:3272px;left:46px;width:267px;height:203px;background:linear-gradient(135deg,#4f4f4f,#2a2a2a)" role="img" aria-label="Student holding a tablet in front of a chalkboard"></div>
  <div class="photo" style="top:3054px;left:325px;width:270px;height:421px;background:linear-gradient(180deg,#3b4a4e,#6b7a55 55%,#b5442e)" role="img" aria-label="Apple on a stack of books before a chalkboard"></div>
  <div class="photo" style="top:3054px;left:604px;width:550px;height:421px;background:linear-gradient(120deg,#cfd6c1,#8aa06c 45%,#6b5a8a)" role="img" aria-label="Two students sharing a tablet outdoors"></div>
</section>

<footer>
  <div class="abs contact"></div>
  <h2 class="abs heading contact-title">Contact Information</h2>
  <div class="abs c-col" style="top:3620px;left:76px">
    <div class="c-icon"><svg width="20" height="26" viewBox="0 0 20 26"><path d="M10 1a8 8 0 0 0-8 8c0 6 8 15 8 15s8-9 8-15a8 8 0 0 0-8-8z" fill="none" stroke="#aab3bf" stroke-width="2"/><circle cx="10" cy="9" r="3" fill="#aab3bf"/></svg></div>
    Willowgate Learning Studio,<br>418 Maple Crest Avenue,<br>Springfield, IL
  </div>
  <div class="abs c-col" style="top:3620px;left:470px">
    <div class="c-icon"><svg width="22" height="22" viewBox="0 0 24 24"><path d="M6 2l4 5-2 3c1 3 3 5 6 6l3-2 5 4-3 4C10 22 2 14 2 5z" fill="#aab3bf"/></svg></div>
    60612<br>555-014-2290
  </div>
  <div class="abs c-col" style="top:3620px;left:862px">
    <div class="c-icon"><svg width="22" height="16" viewBox="0 0 22 16"><rect x="1" y="1" width="20" height="14" fill="none" stroke="#aab3bf" stroke-width="2"/><path d="M1 1l10 8 10-8" fill="none" stroke="#aab3bf" stroke-width="2"/></svg></div>
    info@willowgatestudio.com
  </div>

  <div class="abs query">
    <h2 class="heading">Any Query ? Let's Talk</h2>
    <div class="field" style="top:116px">Full Name</div>
    <div class="field" style="top:175px">Email Address</div>
    <div class="field" style="top:234px">Phone Number</div>
    <div class="message">Your Message</div>
    <div class="submit">SUBMIT</div>
  </div>

  <div class="abs footer">
    <p>Copyright © Willowgate Learning Studio | All Rights Reserved</p>
    <div class="pay-badge"></div>
  </div>
</footer>

</body>
</html>
```